Business Card Design for Real Estate Company

I am looking for a business card design that will catch my client's attention.

Industry/Entity Type

Business

Requirements
Must have
• Please have the following information in the business card design. You can substitute the "Office, Mobile, email, and web" with an icon or some other design you may think will go well with the business card.

Derek Osmund
482 W. Fenwick St., Suite 310
Pasadena, CA 91348
Office: 626.748.1196
Mobile: 626.913.4071
email: Derek@CrestviewPropertyWalk.example
web: www.CrestviewPropertyWalk.example

```html
<!DOCTYPE html>
<html lang="en">
<head>
<meta charset="utf-8">
<title>Crestview Property Walk — Business Card</title>
<link rel="stylesheet" href="https://fonts.googleapis.com/css2?family=Marcellus&display=swap">
<style>
  :root {
    --backdrop: #ebebeb;
    --brown: #5c4a24;
    --paper: #f7f7f5;
    --ink: #4a3c1e;
    --ink-soft: #5a4c30;
    --cream: #f4efe3;
    --leaf-blue: #2f7fc1;
    --leaf-lime: #c9c93a;
    --leaf-orange: #ec8a2c;
    --leaf-olive: #a9b25a;
  }
  * { box-sizing: border-box; margin: 0; padding: 0; }
  html, body {
    width: 1200px;
    height: 795px;
    overflow: hidden;
    background: var(--backdrop);
    font-family: "Marcellus", "Optima", serif;
  }
  .canvas {
    position: relative;
    width: 1200px;
    height: 795px;
  }
  .card {
    position: absolute;
    top: 255px;
    width: 490px;
    height: 280px;
    box-shadow: 0 2px 6px rgba(0,0,0,0.12);
  }
  /* Front side */
  .card--front {
    left: 85px;
    background: var(--brown);
    color: var(--cream);
    display: flex;
    flex-direction: column;
    align-items: center;
    justify-content: center;
  }
  .brand {
    display: flex;
    align-items: center;
    gap: 10px;
  }
  .brand__dot {
    width: 12px;
    height: 12px;
    border-radius: 50%;
    background: currentColor;
  }
  .brand__name {
    font-size: 30px;
    letter-spacing: 0.5px;
  }
  .card--front .web {
    margin-top: 28px;
    font-size: 13px;
    letter-spacing: 0.4px;
  }
  /* Back side */
  .card--back {
    left: 625px;
    background: var(--paper);
    color: var(--ink);
  }
  .card--back .band {
    position: absolute;
    left: 0; top: 0; bottom: 0;
    width: 22px;
    background: var(--brown);
  }
  .card--back .brand {
    position: absolute;
    top: 40px;
    right: 92px;
    color: var(--ink);
  }
  .card--back .brand__name { font-size: 21px; }
  .card--back .brand__dot { width: 9px; height: 9px; }
  .leaves {
    position: absolute;
    top: 26px;
    right: 0;
    width: 72px;
    height: 112px;
    background: linear-gradient(160deg, var(--leaf-olive) 0%, var(--leaf-lime) 40%, var(--leaf-orange) 65%, var(--leaf-blue) 100%);
    opacity: 0.85;
  }
  .contact {
    position: absolute;
    left: 52px;
    bottom: 40px;
  }
  .contact__name {
    font-size: 22px;
    font-weight: 400;
    letter-spacing: 0.3px;
    margin-bottom: 8px;
  }
  .contact__list {
    list-style: none;
    font-size: 13px;
    color: var(--ink-soft);
    line-height: 1.45;
  }
  .contact__list li {
    display: flex;
    align-items: center;
    gap: 8px;
  }
  .contact__list svg { width: 11px; height: 11px; flex: none; }
  .address {
    margin-top: 8px;
    font-style: normal;
    font-size: 13px;
    color: var(--ink-soft);
    line-height: 1.45;
    padding-left: 19px;
  }
</style>
</head>
<body>
<main class="canvas">
  <section class="card card--front" aria-label="Card front">
    <div class="brand">
      <span class="brand__dot"></span>
      <span class="brand__name">Crestview Property Walk</span>
    </div>
    <p class="web">www.CrestviewPropertyWalk.example</p>
  </section>

  <section class="card card--back" aria-label="Card back">
    <div class="band"></div>
    <div class="brand">
      <span class="brand__dot"></span>
      <span class="brand__name">Crestview Property Walk</span>
    </div>
    <div class="leaves" role="img" aria-label="Decorative cluster of colourful leaves in blue, lime, olive and orange"></div>

    <div class="contact">
      <h1 class="contact__name">Derek Osmund</h1>
      <ul class="contact__list">
        <li>
          <svg viewBox="0 0 12 12" aria-label="Office phone"><path d="M3 1 L5 3.5 L4 5 Q5 7 7 8 L8.5 7 L11 9 L9.5 11 Q4 10.5 1 2.5 Z" fill="var(--leaf-orange)"/></svg>
          626.748.1196
        </li>
        <li>
          <svg viewBox="0 0 12 12" aria-label="Mobile"><rect x="3" y="1" width="6" height="10" rx="1" fill="none" stroke="var(--leaf-olive)" stroke-width="1.4"/></svg>
          626.913.4071
        </li>
        <li>
          <svg viewBox="0 0 12 12" aria-label="Email"><rect x="1" y="2.5" width="10" height="7" fill="var(--leaf-blue)"/><path d="M1 2.5 L6 6.5 L11 2.5" fill="none" stroke="#fff" stroke-width="1"/></svg>
          Derek@CrestviewPropertyWalk.example
        </li>
      </ul>
      <address class="address">
        482 W. Fenwick St., Suite 310<br>
        Pasadena, CA 91348
      </address>
    </div>
  </section>
</main>
</body>
</html>
```